Target Market(s)

Young, male, tech savvy, cryptocurrency investors

Industry/Entity Type

Information Technology

Logo Text

Coding

Coded - Design and coding required

Number of Pages Required

1 page

Font styles to use
Sans Serif

Colors

Designer to choose colors to be used in the design.

Requirements
Must have

```html
<!DOCTYPE html>
<html lang="en">
<head>
<meta charset="utf-8">
<title>Kryon Network — Token Distribution</title>
<link href="https://fonts.googleapis.com/css2?family=Nunito:wght@300;400;700;800&display=swap" rel="stylesheet">
<style>
  :root {
    --bg: #0b0b0c;
    --bg-soft: #18191b;
    --accent: #0ea5e6;
    --dot: #2aa7df;
    --white: #ffffff;
    --muted: #d6d6d6;
  }
  * { box-sizing: border-box; margin: 0; padding: 0; }
  html, body { width: 1200px; height: 691px; overflow: hidden; background: var(--bg); }
  body { font-family: "Nunito", sans-serif; color: var(--white); }

  .page { position: relative; width: 1200px; height: 691px; overflow: hidden; }

  .network-backdrop {
    position: absolute; inset: 0;
    background: radial-gradient(ellipse at 50% 45%, var(--bg-soft) 0%, var(--bg) 70%);
  }

  .brand { position: absolute; left: 0; width: 1200px; top: 44px; text-align: center; }
  .brand-square { width: 74px; height: 74px; margin: 0 auto; background: var(--accent); }
  .brand-name { margin-top: 10px; font-size: 22px; font-weight: 700; letter-spacing: -0.5px; color: var(--white); }

  .divider {
    position: absolute; left: 556px; top: 174px; width: 90px; height: 0;
    border-top: 2px dotted var(--accent);
  }

  .headline { position: absolute; left: 0; width: 1200px; top: 199px; text-align: center; }
  .headline-main { font-size: 16.5px; font-weight: 700; color: var(--accent); letter-spacing: 0.1px; }
  .headline-sub { font-size: 16.5px; font-weight: 300; color: var(--white); margin-top: 2px; }

  .timeline-line {
    position: absolute; left: 262px; top: 362px; width: 678px; height: 0;
    border-top: 2px dotted var(--dot);
  }
  .timeline-end {
    position: absolute; top: 355px; width: 15px; height: 15px; border-radius: 50%;
    background: var(--dot);
  }
  .timeline-end.start { left: 249px; }
  .timeline-end.finish { left: 936px; }

  .milestone { position: absolute; top: 292px; width: 240px; margin-left: -120px; text-align: center; }
  .milestone-date { font-size: 14px; font-weight: 400; letter-spacing: -0.4px; height: 29px; }
  .milestone-icon { position: relative; width: 88px; height: 88px; margin: 0 auto; }
  .milestone-frame {
    position: absolute; left: 0; top: 0; width: 80px; height: 86px;
    border: 2px solid var(--white); background: var(--bg);
  }
  .milestone-tile {
    position: absolute; left: 7px; top: 7px; width: 80px; height: 80px;
    border: 2px solid var(--white); border-left-color: transparent; border-top-color: transparent;
  }
  .milestone-fill {
    position: absolute; left: 7px; top: 7px; width: 72px; height: 72px;
    background: var(--accent); display: flex; align-items: center; justify-content: center;
  }
  .milestone-title { margin-top: 21px; font-size: 16px; line-height: 19px; font-weight: 300; }
  .milestone-title strong { font-weight: 800; }

  .signup { position: absolute; left: 0; width: 1200px; top: 529px; text-align: center; }
  .signup-heading { font-size: 16.5px; font-weight: 400; letter-spacing: 1.3px; }
  .signup-heading span { color: var(--accent); font-weight: 800; }

  .signup-form {
    position: absolute; left: 426px; top: 566px; width: 352px; height: 27px;
    border: 1px solid var(--white); border-radius: 3px; display: flex; align-items: center;
  }
  .signup-input {
    flex: 1; background: transparent; border: 0; outline: none; color: var(--white);
    font-family: "Nunito", sans-serif; font-size: 9.5px; padding-left: 12px;
  }
  .signup-input::placeholder { color: var(--white); }
  .signup-submit {
    width: 23px; height: 21px; margin-right: 2px; border: 0; border-radius: 2px;
    background: var(--accent); display: flex; align-items: center; justify-content: center;
  }

  .footer { position: absolute; left: 250px; width: 701px; top: 642px; display: flex; justify-content: space-between; font-size: 8.5px; color: var(--muted); }
  .footer a { color: var(--accent); font-weight: 700; text-decoration: none; }
</style>
</head>
<body>
<div class="page">
  <div class="network-backdrop" role="img" aria-label="Faint background pattern of connected nodes and lines"></div>

  <header class="brand">
    <div class="brand-square"></div>
    <div class="brand-name">KryonNetwork</div>
  </header>

  <div class="divider"></div>

  <section class="headline">
    <h1 class="headline-main">THE WORLD’S MOST ADVANCED BLOCKCHAIN</h1>
    <p class="headline-sub">THE WIDEST TOKEN DISTRIBUTION</p>
  </section>

  <div class="timeline-line"></div>
  <div class="timeline-end start"></div>
  <div class="timeline-end finish"></div>

  <article class="milestone" style="left:352px">
    <div class="milestone-date">Sep 2017</div>
    <div class="milestone-icon">
      <div class="milestone-tile"></div>
      <div class="milestone-frame"></div>
      <div class="milestone-fill"></div>
    </div>
    <div class="milestone-title"><strong>Solvane</strong><br>Network Airdrop</div>
  </article>

  <article class="milestone" style="left:598px">
    <div class="milestone-date">Oct 2017</div>
    <div class="milestone-icon">
      <div class="milestone-tile"></div>
      <div class="milestone-frame"></div>
      <div class="milestone-fill"></div>
    </div>
    <div class="milestone-title"><strong>Quorvex</strong> Network Linked<br>Address Airdrop</div>
  </article>

  <article class="milestone" style="left:845px">
    <div class="milestone-date">Nov 2017</div>
    <div class="milestone-icon">
      <div class="milestone-tile"></div>
      <div class="milestone-frame"></div>
      <div class="milestone-fill">
        <svg width="56" height="34" viewBox="0 0 56 34" aria-hidden="true">
          <path d="M2 17 C12 3 44 3 54 17 C44 31 12 31 2 17 Z" fill="#fff"/>
          <circle cx="28" cy="17" r="11" fill="var(--accent)"/>
          <path d="M22.5 17.5 L26.5 21.5 L33.5 13.5" fill="none" stroke="#fff" stroke-width="3" stroke-linecap="round" stroke-linejoin="round"/>
        </svg>
      </div>
    </div>
    <div class="milestone-title"><strong>Proof-of-Individuality</strong><br>Human Airdrop</div>
  </article>

  <section class="signup">
    <h2 class="signup-heading"><span>SIGN UP</span> NOW</h2>
  </section>

  <form class="signup-form" action="#">
    <input class="signup-input" type="email" placeholder="Enter your email address">
    <button class="signup-submit" type="button" aria-label="Submit">
      <svg width="11" height="10" viewBox="0 0 11 10" aria-hidden="true">
        <path d="M1 5 H9.5 M6 1.5 L9.5 5 L6 8.5" fill="none" stroke="#fff" stroke-width="1.6" stroke-linecap="round" stroke-linejoin="round"/>
      </svg>
    </button>
  </form>

  <footer class="footer">
    <span>Copyright © 2017 Kryon Network. All Rights Reserved.</span>
    <span>Built By <a href="#">Brightpath Studio</a></span>
  </footer>
</div>
</body>
</html>
```